Gavin Holloway Advisory - Web Design Project

We need a web design for my new edgy consulting business specializing in innovation, technology and strategy.

It is our personal goal to turn each client into raving fans by helping them achieve their own business goals and aspirations through assisting them in raising their own innovation and marketing standards.

We provide our personalised and state-of-the-art services to our clients and boards who represent some of the world greatest innovative thinkers.

Here is some other information which may help shape your thinking.

I've had direct Involvement in the development of the following iPad, iPhone Applications and websites

PelicanTrailsHub.com (TerraLoom platform) by Coastline Visitor Bureau
http://pelicantrailshub.example

Harbor Zest by Tidy Sailways
https://apps.example.net/au/app/harbor-zest/id900111222

RedDustGo by Frontier Visits Office
https://apps.example.net/au/app/reddustgo/id900111333

Wexbridge Rambles
http://www.wexbridgerambles.example

Trip Weaver by Coastline Visitor Bureau
http://apps.example.net/au/app/trip-weaver/id900111444

Sunward by Sunward Travel Board
https://apps.example.net/au/app/sunward/id900111555

Fernvale Ridge Road Loop by Roamwell Agency
https://apps.example.net/au/app/fernvale-ridge-road-loop/id900111666

Pathfinder Run by Frontier Visits Office and Southern Coast Visitor Council
https://apps.example.net/au/app/pathfinder-run-grand-trek/id900111777

Gavin Holloway Advisory (GHA)
November 2012 – Present (8 months)Brisbane, Sydney, Canberra

Gavin’s consults to Small-to-Medium Enterprises (SME) and Government organisations on business strategy, technology strategy, risk mitigation, disruptive technology and innovation in the workplace.

Gavin’s consultancy mantra is that we cannot divorce economic life from cultural life particularly in an era when social capital may be as important as physical capital in business.

Reason: request from designers, I want to see their best efforts

Target Market(s)

35+

Industry/Entity Type

Business

Requirements
Must have
• Please use some of the personal image(s) contained in the zip files which can be downloaded from here

http://filedrop.example/k7Pq2Lm9
http://filedrop.example/r4Tz8Hv1
http://filedrop.example/w6Nc3Bx5
Nice to have
• Black, Sleek design, maybe minimalist. Nice to have a Glint for the design. Nice to have it easily ported to Wordpress or be a modified Wordpress template. HTML 5, responsive design

```html
<!DOCTYPE html>
<html lang="en">
<head>
<meta charset="utf-8">
<title>Gavin Holloway Advisory</title>
<link href="https://fonts.googleapis.com/css2?family=Carlito:wght@400;700&family=Tinos&display=swap" rel="stylesheet">
<style>
:root{
  --orange:#d4500f;
  --ink:#111;
  --text:#333;
  --muted:#8a8a8a;
  --line:#dcdcdc;
  --page:#f7f7f7;
  --bar:#e4e4e4;
  --white:#fff;
}
*{margin:0;padding:0;box-sizing:border-box}
html,body{width:1120px;height:1200px;overflow:hidden}
body{font-family:"Carlito",sans-serif;background:var(--page);color:var(--text);position:relative}
.abs{position:absolute}
.top-strip{left:0;top:0;width:1120px;height:4px;background:#d9d9d9}
.callback-bar{left:184px;top:5px;width:750px;height:27px;background:var(--bar);display:flex;align-items:center;padding-left:13px;font-family:"Tinos",serif;font-size:9px;color:#555;letter-spacing:.2px}
.callback-bar input{margin-left:10px;width:88px;height:16px;border:1px solid #ccc;font-size:8px;padding-left:6px;font-family:"Carlito",sans-serif}
.callback-bar .send{margin-left:5px;background:var(--orange);color:#fff;font-family:"Carlito",sans-serif;font-weight:700;font-size:9px;width:35px;height:16px;display:flex;align-items:center;justify-content:center}
.social{display:flex;gap:4px;margin-left:10px}
.social span{width:15px;height:15px;border-radius:50%;background:#c9c9c9}
.callback-bar .toggle{margin-left:auto;width:18px;height:27px;background:#d4d4d4;display:flex;align-items:center;justify-content:center}
.brand{left:182px;top:44px;font-size:33px;font-weight:700;letter-spacing:-.3px;color:var(--ink)}
.brand .first{color:var(--orange)}
.contact{left:720px;top:48px;display:flex;gap:8px;align-items:center}
.contact .phone-ico{width:27px;height:27px;border-radius:50%;background:#222;display:flex;align-items:center;justify-content:center}
.contact strong{display:block;font-size:15px;color:var(--ink);font-weight:700;line-height:1}
.contact small{font-size:11px;color:var(--muted);line-height:1.3}
.nav-band{left:0;top:94px;width:1120px;height:47px;background:var(--white);border-bottom:1px solid var(--line)}
.nav{left:183px;top:94px;height:47px;display:flex;align-items:center;font-size:12px;color:var(--ink)}
.nav a{text-decoration:none;color:inherit;margin-right:30px;position:relative;height:47px;display:flex;align-items:center}
.nav a.active{color:var(--orange)}
.nav a.active::after{content:"";position:absolute;left:0;right:0;bottom:0;height:3px;background:var(--orange)}
.search{left:782px;top:107px;width:152px;height:19px;border:1px solid #ddd;background:#fafafa;font-size:8px;color:#aaa;display:flex;align-items:center;padding-left:8px}
.search .btn{margin-left:auto;width:20px;height:17px;border-left:1px solid #ddd;display:flex;align-items:center;justify-content:center}
.hero{left:0;top:141px;width:1120px;height:393px;background:linear-gradient(180deg,#fbfbfb 0%,#f1f1f1 55%,#e9e9e9 100%);border-bottom:3px solid #ececec}
.hero-skyline{left:0;top:265px;width:1120px;height:128px;background:linear-gradient(180deg,rgba(225,225,225,.2),rgba(215,215,215,.7))}
.hero-portrait{left:184px;top:23px;width:298px;height:370px;background:linear-gradient(180deg,#e9e6e3 0%,#d8d0c8 40%,#2a2a2a 70%,#1a1a1a 100%)}
.hero-title{left:538px;top:72px;font-size:39px;font-weight:700;color:var(--orange);line-height:1.08}
.hero-sub{left:537px;top:178px;font-size:15.5px;font-weight:700;color:var(--ink)}
.hero-sub em{font-style:normal;color:#8a8a8a}
.hero-text{left:537px;top:209px;width:392px;font-size:10px;line-height:13.6px;color:#777}
.hero-btn{left:538px;top:293px;width:94px;height:31px;background:var(--ink);color:#fff;font-size:13px;font-weight:700;display:flex;align-items:center;justify-content:center}
.slide-arrow{width:30px;height:26px;display:flex;align-items:center;justify-content:center}
.slide-arrow.prev{left:0;background:#efc9b2}
.slide-arrow.next{left:1090px;background:#cfcfcf}
.specialty{top:563px;width:226px;text-align:center}
.specialty h3{font-size:17px;font-weight:400;color:var(--ink);line-height:20px}
.specialty h3 span{display:block;color:var(--orange)}
.specialty p{font-size:10px;color:#999;line-height:13.6px;margin-top:9px}
.specialty .more{margin:15px auto 0;width:118px;height:21px;background:var(--ink);color:#fff;font-size:10px;font-weight:700;border-radius:3px;display:flex;align-items:center;justify-content:center;box-shadow:0 -2px 8px rgba(0,0,0,.06)}
.section-head{font-size:14px;color:var(--ink);display:flex;align-items:center;font-weight:400}
.section-head::after{content:"";flex:1;margin-left:16px;border-top:1px dashed #ccc}
.section-head .arrows{order:2;margin-left:6px;font-size:10px;color:#bbb}
.project{top:761px;width:240px;height:215px;background:var(--white);border-bottom:2px solid var(--orange);text-align:center}
.project .img{height:136px}
.project h4{font-size:14px;font-weight:400;color:var(--ink);margin-top:8px}
.project p{font-size:10px;color:#888;line-height:13.6px;margin-top:3px;padding:0 17px}
.news{top:1045px;width:175px;height:155px;background:var(--white);border:1px solid #eee}
.news .img{height:103px}
.news .meta{display:flex;justify-content:space-between;align-items:baseline;padding:9px 11px 0}
.news .meta b{font-weight:400;font-size:11.5px;color:var(--ink)}
.news .meta small{font-size:8.5px;color:#999}
.news p{font-size:8.5px;color:#999;line-height:12px;padding:3px 11px 0}
.news p i{color:var(--orange)}
.faq{left:569px;top:1045px;width:365px;height:155px;background:var(--white);border:1px solid #e2e2e2}
.faq .item{height:32px;display:flex;align-items:center;justify-content:space-between;padding:0 14px;font-size:12px;color:var(--ink);border-bottom:1px solid #e2e2e2}
.faq .item.open{border-bottom:2px solid var(--orange)}
.faq .answer{height:64px;padding:7px 14px;font-size:9px;line-height:12.6px;color:#777;text-align:justify;border-bottom:1px solid #e2e2e2}
.dot{width:12px;height:12px;border-radius:50%;background:#555;display:flex;align-items:center;justify-content:center}
</style>
</head>
<body>
<div class="abs top-strip"></div>

<div class="abs callback-bar">
  ENTER YOUR PHONE NUMBER HERE AND WE CALL YOU IN THE NEXT FEW HOURS:
  <input value="+00 000-0000" aria-label="Phone number">
  <span class="send">Send</span>
  <div class="social"><span></span><span></span><span></span><span></span><span></span></div>
  <span class="toggle"><svg width="7" height="5" viewBox="0 0 7 5"><path d="M0.5 4.5 3.5 1.5 6.5 4.5" fill="none" stroke="#fff" stroke-width="1.3"/></svg></span>
</div>

<div class="abs brand"><span class="first">GAVIN</span> HOLLOWAY</div>

<div class="abs contact">
  <span class="phone-ico"><svg width="14" height="14" viewBox="0 0 24 24"><path fill="#fff" d="M6.6 10.8c1.4 2.8 3.8 5.1 6.6 6.6l2.2-2.2c.3-.3.7-.4 1-.2 1.1.4 2.3.6 3.6.6.6 0 1 .4 1 1V20c0 .6-.4 1-1 1C10.6 21 3 13.4 3 4c0-.6.4-1 1-1h3.5c.6 0 1 .4 1 1 0 1.3.2 2.5.6 3.6.1.3 0 .7-.2 1z"/></svg></span>
  <div><strong>Call Us: +000 555 01.23.456</strong><small>7/7days &nbsp;9am-11pm</small></div>
</div>

<div class="abs nav-band"></div>
<nav class="abs nav">
  <a class="active">Home</a><a>About Us</a><a>Consultations</a><a>Services</a><a>FAQ</a><a>Contact Us</a>
</nav>
<div class="abs search">Search<span class="btn"><svg width="8" height="8" viewBox="0 0 10 10"><circle cx="4" cy="4" r="3" fill="none" stroke="#aaa" stroke-width="1.3"/><path d="M6.3 6.3 9 9" stroke="#aaa" stroke-width="1.3"/></svg></span></div>

<section class="abs hero">
  <div class="abs hero-skyline" role="img" aria-label="Faint city skyline with a rising line chart"></div>
  <div class="abs hero-portrait" role="img" aria-label="Portrait of Gavin Holloway in a dark suit and tie"></div>
  <h1 class="abs hero-title">SOLUTIONS,<br>THAT YOU NEED?</h1>
  <h2 class="abs hero-sub">BE SUCESSFULL IT’S <em>EASY</em>! &nbsp;FOR YOUR <em>BUSINESS</em></h2>
  <p class="abs hero-text">Lorem Ipsum is simply dummy text of the printing and typesetting industry. Lorem Ipsum has been the industry's standard dummy text ever since the 1500s, when an unknown printer took a galley of type and scrambled it to make a type specimen book Lorem Ipsum is simply dummy text of the printing.</p>
  <div class="abs hero-btn">View Details</div>
  <div class="abs slide-arrow prev" style="top:185px"><svg width="6" height="9" viewBox="0 0 6 9"><path d="M5 1 1.5 4.5 5 8" fill="none" stroke="#fff" stroke-width="1.5"/></svg></div>
  <div class="abs slide-arrow next" style="top:185px"><svg width="6" height="9" viewBox="0 0 6 9"><path d="M1 1 4.5 4.5 1 8" fill="none" stroke="#fff" stroke-width="1.5"/></svg></div>
</section>

<div class="abs specialty" style="left:183px"><h3>Specializing In<span>Innovation</span></h3><p>Lorem Ipsum is simply dummy text of the printing and typesetting industry. Lorem Ipsum has been the industry's standard dummy.</p><div class="more">Read More</div></div>
<div class="abs specialty" style="left:447px"><h3>Specializing In<span>Technology</span></h3><p>Lorem Ipsum is simply dummy text of the printing and typesetting industry. Lorem Ipsum has been the industry's standard dummy.</p><div class="more">Read More</div></div>
<div class="abs specialty" style="left:709px"><h3>Specializing In<span>Strategy</span></h3><p>Lorem Ipsum is simply dummy text of the printing and typesetting industry. Lorem Ipsum has been the industry's standard dummy.</p><div class="more">Read More</div></div>

<h2 class="abs section-head" style="left:183px;top:730px;width:751px">RECENT PROJECTS<span class="arrows">‹ ›</span></h2>

<article class="abs project" style="left:184px"><div class="img" role="img" aria-label="Hand touching a tablet screen" style="background:linear-gradient(160deg,#e8dccb,#b89a78 50%,#3a3a3a)"></div><h4>Lorem Ipsum</h4><p>Lorem Ipsum as their default model text, and a search will uncover many web sites still their word in literature.</p></article>
<article class="abs project" style="left:439px"><div class="img" role="img" aria-label="Finger tapping a tablet on a desk" style="background:linear-gradient(160deg,#dfe2e8,#c6b8aa 50%,#6d6f74)"></div><h4>Lorem Ipsum</h4><p>Lorem Ipsum as their default model text, and a search will uncover many web sites still their word in literature.</p></article>
<article class="abs project" style="left:694px"><div class="img" role="img" aria-label="Business team gathered around a presentation" style="background:linear-gradient(160deg,#eeeeee,#b9a594 50%,#3c3c40)"></div><h4>Lorem Ipsum</h4><p>Lorem Ipsum as their default model text, and a search will uncover many web sites still their word in literature.</p></article>

<h2 class="abs section-head" style="left:182px;top:1016px;width:370px">LATEST NEWS<span class="arrows">‹ ›</span></h2>
<h2 class="abs section-head" style="left:569px;top:1016px;width:365px">WHY CHOOSE US</h2>

<article class="abs news" style="left:184px"><div class="img" role="img" aria-label="Headshot of Gavin Holloway" style="background:linear-gradient(180deg,#f4f4f4,#d6cbc1 55%,#2b2b2b)"></div><div class="meta"><b>Lorem Ipsum</b><small>March 12, 2013</small></div><p>Lorem Ipsum as their default model text, and a search will . <i>more</i></p></article>
<article class="abs news" style="left:375px"><div class="img" role="img" aria-label="Smiling headshot of Gavin Holloway" style="background:linear-gradient(180deg,#e9eef2,#d2c6bb 55%,#5a6068)"></div><div class="meta"><b>Lorem Ipsum</b><small>March 12, 2013</small></div><p>Lorem Ipsum as their default model text, and a search will . <i>more</i></p></article>

<div class="abs faq">
  <div class="item open">Lorem Ipsum?<span class="dot"><svg width="6" height="4" viewBox="0 0 6 4"><path d="M.5 3.5 3 1l2.5 2.5" fill="none" stroke="#fff" stroke-width="1.2"/></svg></span></div>
  <div class="answer">Lorem Ipsum is simply dummy text of the printing and typesetting industry. Lorem Ipsum has been the industry's standard dummy text ever since the 1500s, when an unknown printer took a galley of type and scrambled it to make a type specimen book.</div>
  <div class="item">Lorem Ipsum Dolar sit?<span class="dot"><svg width="6" height="4" viewBox="0 0 6 4"><path d="M.5.5 3 3 5.5.5" fill="none" stroke="#fff" stroke-width="1.2"/></svg></span></div>
  <div class="item" style="border-bottom:0">Why Us?<span class="dot"><svg width="6" height="4" viewBox="0 0 6 4"><path d="M.5.5 3 3 5.5.5" fill="none" stroke="#fff" stroke-width="1.2"/></svg></span></div>
</div>
</body>
</html>
```